Quillmera

Business cards and core flute signage. The business is only in its infant as a 'market' business. I would like the name to be curved across the page in different colours with a bold line underneath finished with an exotic pen drawing the line. (Similar to pictures)
We are trying to reach all markets as they are designer pens and items are made as requested or they can select from already manufactured pens on display.
I have included some images of the actual pens that I make for inspiration, we are very open to your ideas and guidance if you have a specific design in mind.
If you would more pen photo options, please contact me with your email details.
Darren Talbiro
Pen Maker & Wood Turner
Ph. 0438 271 546
Target Market(s)
Generally professional customers who would use a pen for work on a daily basis
Industry/Entity Type
Business
Requirements
Must have
- Punchy and catchy styling
Nice to have
- One of my pens

```html
<!DOCTYPE html>
<html lang="en">
<head>
<meta charset="utf-8">
<title>Quillmera – Business Card</title>
<link href="https://fonts.googleapis.com/css2?family=Bree+Serif&family=Raleway:wght@200&display=swap" rel="stylesheet">
<style>
  :root {
    --backdrop: #5f5f5f;
    --brand-yellow: #c1b102;
    --card-black: #070707;
    --logo-grey: #5a5847;
    --text-white: #ffffff;
    --pen-amber: #c9501a;
    --pen-deep: #7a2a0e;
    --pen-bronze: #8c7a5a;
  }
  * { margin: 0; padding: 0; box-sizing: border-box; }
  html, body {
    width: 1200px;
    height: 1000px;
    overflow: hidden;
    background: var(--backdrop);
  }
  .business-card {
    position: absolute;
    left: 62px;
    top: 174px;
    width: 1076px;
    height: 652px;
    overflow: hidden;
    background: var(--card-black);
  }
  .brand-band {
    position: absolute;
    left: 0; top: 0;
    width: 100%;
    height: 367px;
    background: var(--brand-yellow);
  }
  .brand-name {
    position: absolute;
    left: 0; top: 0;
    width: 1076px;
    height: 367px;
  }
  .brand-name text {
    font-family: "Bree Serif", Georgia, serif;
    font-size: 100px;
    fill: var(--logo-grey);
  }
  .contact-line {
    position: absolute;
    left: 0;
    width: 1076px;
    text-align: center;
    line-height: 1;
    white-space: nowrap;
  }
  .person-name {
    top: 395px;
    font-family: "Bree Serif", Georgia, serif;
    font-size: 76px;
    color: var(--brand-yellow);
  }
  .person-role {
    top: 492px;
    font-family: "Bree Serif", Georgia, serif;
    font-size: 52px;
    color: var(--text-white);
  }
  .person-role .amp { color: var(--brand-yellow); }
  .person-phone {
    top: 562px;
    font-family: "Raleway", Arial, sans-serif;
    font-weight: 200;
    font-size: 46px;
    color: var(--text-white);
  }
  .person-phone .number { color: var(--brand-yellow); }
  .pen-photo {
    position: absolute;
    left: 0; top: 0;
    width: 1076px;
    height: 652px;
  }
</style>
</head>
<body>
  <div class="business-card">
    <div class="brand-band"></div>

    <svg class="brand-name" viewBox="0 0 1076 367" aria-label="Quillmera">
      <path id="brandArc" d="M 250 250 Q 490 150 730 250" fill="none"/>
      <text text-anchor="middle"><textPath href="#brandArc" startOffset="50%">Quillmera</textPath></text>
    </svg>

    <p class="contact-line person-name">Darren Talbiro</p>
    <p class="contact-line person-role">Pen Maker <span class="amp">&amp;</span> Wood Turner</p>
    <p class="contact-line person-phone">Ph. <span class="number">0438 271 546</span></p>

    <svg class="pen-photo" viewBox="0 0 1076 652" role="img" aria-label="Photograph of a handmade ballpoint pen with an orange acrylic barrel and antique-bronze fittings, set diagonally">
      <defs>
        <linearGradient id="penTone" x1="0" y1="0" x2="0" y2="1">
          <stop offset="0" stop-color="var(--pen-bronze)"/>
          <stop offset="0.22" stop-color="var(--pen-deep)"/>
          <stop offset="0.5" stop-color="var(--pen-amber)"/>
          <stop offset="0.72" stop-color="var(--pen-deep)"/>
          <stop offset="1" stop-color="var(--pen-bronze)"/>
        </linearGradient>
      </defs>
      <rect x="-40" y="0" width="80" height="605" rx="10"
            transform="translate(1016 18) rotate(13)" fill="url(#penTone)"/>
    </svg>
  </div>
</body>
</html>
```